Stylish Homeware business needs a Logo and Business Card design

We need a logo and business card for a new company based in Hong Kong called "Nest Lumora". We do marketing and distributing international stylish Homeware brands in Asia. Products we handle included clocks, picture frame, small kitchen wares, LED lightenings, stationary and etc. We planned to also create our own brands next step. We could like to see designs that use pastel colors. The final design shoudl be simple and stylish.
Target Market(s)
Asia, Mainly Japan, China and Korea
Industry/Entity Type
Business
Contact Information for Business Card
We could like to see designs that use pastel colors. The final design shoudl be simple and stylish. We attach some log design we like on the bottom of the page.
Font styles to use
Look and feel
Each slider illustrates characteristics of the customer's brand and the style your logo design should communicate.

```html
<!DOCTYPE html>
<html lang="en">
<head>
<meta charset="utf-8">
<title>Nest Lumora – Business Card</title>
<link href="https://fonts.googleapis.com/css2?family=Source+Sans+3:wght@400;600&display=swap" rel="stylesheet">
<style>
  :root {
    --backdrop: #111111;
    --card-white: #ffffff;
    --brand-blue: #0a3a8f;
    --ink-grey: #4a4a4a;
  }
  html, body {
    margin: 0;
    padding: 0;
    width: 1200px;
    height: 900px;
    overflow: hidden;
    background: var(--backdrop);
    font-family: "Source Sans 3", "Myriad Pro", sans-serif;
  }
  .stage {
    position: relative;
    width: 1200px;
    height: 900px;
  }
  .card {
    position: absolute;
    top: 306px;
    width: 440px;
    height: 271px;
    border-radius: 12px;
  }
  .card--front {
    left: 149px;
    background: var(--card-white);
  }
  .card--back {
    left: 608px;
    background: var(--brand-blue);
  }
  .wordmark {
    position: absolute;
    display: flex;
    align-items: center;
    gap: 8px;
    font-weight: 600;
    white-space: nowrap;
  }
  .wordmark__dot {
    border-radius: 50%;
    flex: none;
  }
  .card--front .wordmark {
    left: 34px;
    top: 118px;
    font-size: 27px;
    line-height: 34px;
    color: var(--brand-blue);
  }
  .card--front .wordmark__dot {
    width: 10px;
    height: 10px;
    background: var(--brand-blue);
  }
  .card--back .wordmark {
    left: 0;
    right: 0;
    top: 112px;
    justify-content: center;
    font-size: 40px;
    line-height: 48px;
    color: var(--card-white);
  }
  .card--back .wordmark__dot {
    width: 14px;
    height: 14px;
    background: var(--card-white);
  }
  .contact {
    position: absolute;
    left: 238px;
    top: 77px;
    color: var(--ink-grey);
    font-size: 13px;
    line-height: 15.5px;
  }
  .contact__name {
    margin: 0;
    color: var(--brand-blue);
    font-size: 16px;
    font-weight: 600;
    line-height: 18px;
  }
  .contact__role { margin: 0 0 11px; }
  .contact__address { margin: 0 0 12px; font-style: normal; }
  .contact__list { list-style: none; margin: 0; padding: 0; }
  .contact__item {
    display: flex;
    align-items: center;
    gap: 7px;
    height: 15.5px;
  }
  .contact__icon {
    width: 9px;
    height: 9px;
    fill: var(--brand-blue);
    flex: none;
  }
</style>
</head>
<body>
<main class="stage">
  <section class="card card--front" aria-label="Business card front">
    <div class="wordmark">
      <span class="wordmark__dot"></span>
      <span class="wordmark__name">Nest Lumora</span>
    </div>
    <div class="contact">
      <p class="contact__name">Marcus Ellery</p>
      <p class="contact__role">Managing Director</p>
      <address class="contact__address">48 Harbour View Road<br>Kowloon, Hong Kong 999077.</address>
      <ul class="contact__list">
        <li class="contact__item">
          <svg class="contact__icon" viewBox="0 0 10 10" aria-hidden="true"><path d="M2 0.5 L3.8 2.6 L2.9 3.8 Q4 6 6.2 7.1 L7.4 6.2 L9.5 8 L8.3 9.5 Q4.5 9.5 2 7 Q0.5 4.5 0.5 1.7 Z"/></svg>
          <span>852-2468 1357</span>
        </li>
        <li class="contact__item">
          <svg class="contact__icon" viewBox="0 0 10 10" aria-hidden="true"><rect x="0.5" y="2" width="9" height="6.5"/><path d="M0.5 2 L5 5.6 L9.5 2" stroke="#fff" stroke-width="0.9" fill="none"/></svg>
          <span>hello@nestlumora.com</span>
        </li>
        <li class="contact__item">
          <svg class="contact__icon" viewBox="0 0 10 10" aria-hidden="true"><circle cx="5" cy="5" r="4.6"/><path d="M0.6 5 H9.4 M5 0.5 Q2.5 5 5 9.5 M5 0.5 Q7.5 5 5 9.5" stroke="#fff" stroke-width="0.7" fill="none"/></svg>
          <span>www.nestlumora.com</span>
        </li>
      </ul>
    </div>
  </section>
  <section class="card card--back" aria-label="Business card back">
    <div class="wordmark">
      <span class="wordmark__dot"></span>
      <span class="wordmark__name">Nest Lumora</span>
    </div>
  </section>
</main>
</body>
</html>
```